Australian Wine export company Need a Wine label design

We need a wine label design for a new branded Australian wine based in South Australia called " HALLORAN " .
We will use this brand name ' HALLORAN' to marketing Australian Red wine and White wine into Chinese Market.
We would like to see the label designs that look classic and make consumers feel this is a superior quality Australian wine.
This label is to promote AUSTRALIAN WINE, need wine related and country related theme, need to give the consumer first impression that this wine is from AUSTRALIA.

Thanks
Updates

The following information are required to be presented on the wine label:

1) Brand Name: Halloran
2) Logo
3) Year of Vintage
4) Varietal
5) Place of production: South Australia
6) Fine Wine of Australia

Thanks.

Target Market(s)

Chinese market

Industry/Entity Type

Marketing

Requirements
Must have
• Need label design and renderings on the bottles.
Nice to have
• Label make consumers feel this is a superior quality Australian Wine.

```html
<!DOCTYPE html>
<html lang="en">
<head>
<meta charset="utf-8">
<title>Halloran – Cabernet Sauvignon 2012 labels</title>
<link rel="stylesheet" href="https://fonts.googleapis.com/css2?family=Cinzel:wght@400;600&family=Crimson+Text:ital,wght@0,400;0,600;1,400&family=Roboto+Condensed:wght@400&display=swap">
<style>
  :root {
    --page: #ececea;
    --paper: #f6f6f3;
    --ink: #2b2b2b;
    --ink-soft: #4a4a48;
    --gold: #a9a01c;
    --gold-dark: #8c8412;
    --gold-light: #e6dfa2;
    --rule: #9a9a96;
  }
  * { margin: 0; padding: 0; box-sizing: border-box; }
  html, body { width: 1200px; height: 900px; overflow: hidden; background: var(--page); }
  .canvas { position: relative; width: 1200px; height: 900px; }

  .label {
    position: absolute;
    background: var(--paper);
    color: var(--ink);
    font-family: "Crimson Text", Georgia, serif;
    text-align: center;
    box-shadow: 0 1px 4px rgba(0,0,0,.12);
  }
  .label--front-full { left: 224px; top: 390px; width: 213px; height: 255px; }
  .label--front-plain { left: 510px; top: 390px; width: 213px; height: 255px; }
  .label--back { left: 820px; top: 393px; width: 212px; height: 217px; }

  .brand-mark {
    position: absolute; left: 50%; transform: translateX(-50%);
    border-radius: 50%;
    background: var(--gold);
  }
  .label--front-full .brand-mark,
  .label--front-plain .brand-mark { top: 22px; width: 18px; height: 18px; }
  .label--back .brand-mark { top: 9px; width: 10px; height: 10px; }

  .brand-name {
    position: absolute; left: 0; right: 0;
    font-family: "Cinzel", "Times New Roman", serif;
    font-weight: 400;
    letter-spacing: 4px;
    color: var(--ink);
  }
  .label--front-full .brand-name,
  .label--front-plain .brand-name { top: 64px; font-size: 21px; }
  .label--back .brand-name { top: 28px; font-size: 10.5px; letter-spacing: 2px; font-weight: 600; }

  .wine-details {
    position: absolute; left: 0; right: 0;
    font-size: 13px; line-height: 18.5px; letter-spacing: 1px;
  }
  .label--front-full .wine-details { top: 117px; }
  .label--front-plain .wine-details { top: 126px; }

  .tasting-note {
    position: absolute; left: 30px; right: 30px; top: 188px;
    font-style: italic; font-size: 5.6px; line-height: 7px; color: var(--ink-soft);
  }
  .volume {
    position: absolute; right: 18px; top: 208px;
    font-size: 9.5px;
  }
  .origin-band {
    position: absolute; left: 0; right: 0; bottom: 0; height: 26px;
    background: linear-gradient(180deg, var(--gold) 0%, var(--gold-dark) 100%);
    color: var(--gold-light);
    font-size: 7px; letter-spacing: 1px; line-height: 26px;
  }

  /* back label */
  .back-intro {
    position: absolute; left: 14px; right: 14px; top: 43px;
    font-size: 8px; line-height: 10px;
  }
  .back-rule {
    position: absolute; left: 10px; right: 10px; height: 1px; background: var(--rule);
  }
  .back-rule--upper { top: 79px; }
  .back-rule--lower { top: 146px; }
  .back-title {
    position: absolute; left: 0; right: 0; top: 83px;
    font-size: 8.5px; font-weight: 600;
  }
  .back-notes {
    position: absolute; left: 14px; right: 14px; top: 96px;
    font-size: 7.4px; line-height: 8.7px;
  }
  .statutory {
    position: absolute; left: 8px; top: 151px;
    list-style: none; text-align: left;
    font-family: "Roboto Condensed", Arial, sans-serif;
    font-size: 5.6px; line-height: 8.3px; letter-spacing: .3px; text-transform: uppercase;
  }
  .label--back .volume { top: 148px; right: 10px; font-size: 12.5px; }
</style>
</head>
<body>
<main class="canvas">

  <section class="label label--front-full" aria-label="Front label with tasting note">
    <span class="brand-mark"></span>
    <h1 class="brand-name">HALLORAN</h1>
    <p class="wine-details">South Australia<br>Cabernet Sauvignon<br>2012</p>
    <p class="tasting-note">Mauris eros neque, lacinia eu mi non, pellentesque vulputate tortor. Nunc tincidunt non nulla eu scelerisque. Quisque ac leo purus.</p>
    <p class="volume">750ml</p>
    <p class="origin-band">FINE WINE OF AUSTRALIA</p>
  </section>

  <section class="label label--front-plain" aria-label="Front label">
    <span class="brand-mark"></span>
    <h2 class="brand-name">HALLORAN</h2>
    <p class="wine-details">South Australia<br>Cabernet Sauvignon<br>2012</p>
    <p class="volume">750ml</p>
    <p class="origin-band">FINE WINE OF AUSTRALIA</p>
  </section>

  <section class="label label--back" aria-label="Back label">
    <span class="brand-mark"></span>
    <h2 class="brand-name">HALLORAN</h2>
    <p class="back-intro">Lorem ipsum dolor sit amet, consectetur adipiscing elit. Quisque pharetra quam nec rhoncus tincidunt. Fusce sit amet bibendum.</p>
    <span class="back-rule back-rule--upper"></span>
    <h3 class="back-title">Cabernet Sauvignon 2012</h3>
    <p class="back-notes">Mauris eros neque, lacinia eu mi non, pellentesque vulputate tortor. Nunc tincidunt non nulla eu scelerisque. Quisque ac leo purus. Curabitur vel dui at eros interdum euismod. Nam egestas et arcu et pellentesque.</p>
    <span class="back-rule back-rule--lower"></span>
    <ul class="statutory">
      <li>Produced by Halloran Wines</li>
      <li>Address line 1</li>
      <li>Address line 2</li>
      <li>14.5% alc/vol</li>
      <li>Approx 8.3 standard drinks</li>
      <li>Contains sulphites</li>
      <li>Wine of Australia</li>
    </ul>
    <p class="volume">750ml</p>
  </section>

</main>
</body>
</html>
```